Rebranding our business - Business Cards

We are currently rebranding our business and have just completed our new logo and now are wanting to have new business cards designed.

I will upload our old business card design as we would like to keep the same information on the card, Including the icon dot points on the back. I will also upload other designs I would like placed on the cards.. Such as a character,

I would like our power statement to be:
KTW Removals -The Gentle Movers.

Instead of: Allow KTW Removals To Carry the Weight Of Every Relocation,

I am happy for the designer to run with their own ideas.

```html
<!DOCTYPE html>
<html lang="en">
<head>
<meta charset="utf-8">
<title>KTW Removals – Business Cards</title>
<link rel="stylesheet" href="https://fonts.googleapis.com/css2?family=Open+Sans:wght@400;600;700&display=swap">
<style>
  :root {
    --bg: #e9e7e3;
    --white: #ffffff;
    --navy: #1f2a78;
    --brand-blue: #2a5aa8;
    --sky-top: #3fa3e6;
    --sky-bottom: #1566b8;
    --orange: #e8782e;
    --ink: #555a62;
    --icon: #2f6fb6;
    --figure-a: #f08a3c;
    --figure-b: #3a3a3a;
  }
  * { margin: 0; padding: 0; box-sizing: border-box; }
  html, body { width: 1200px; height: 843px; overflow: hidden; }
  body {
    background: var(--bg);
    font-family: "Open Sans", Arial, sans-serif;
    position: relative;
  }
  .card {
    position: absolute;
    top: 266px;
    width: 540px;
    height: 310px;
    border-radius: 4px;
    box-shadow: 0 8px 22px rgba(0,0,0,0.22);
    overflow: hidden;
  }

  /* Front */
  .card-front { left: 40px; background: var(--white); }
  .front-band {
    position: absolute; right: 0; top: 0; bottom: 0; width: 44px;
    background: var(--navy);
    display: flex; align-items: center; justify-content: center;
  }
  .front-band .tagline {
    color: var(--white); font-size: 12px; white-space: nowrap;
    transform: rotate(-90deg);
    letter-spacing: 0.2px;
  }
  .brand {
    position: absolute; left: 44px; top: 28px;
    display: flex; align-items: center; gap: 10px;
  }
  .brand-dot { width: 18px; height: 18px; border-radius: 50%; background: var(--navy); }
  .brand-name { font-size: 30px; font-weight: 600; color: var(--brand-blue); line-height: 1; }
  .brand-sub {
    position: absolute; left: 72px; top: 66px;
    font-size: 12px; color: var(--ink); letter-spacing: 1.5px;
  }
  .contact {
    position: absolute; left: 44px; top: 118px;
    list-style: none; font-size: 14px; color: var(--ink);
  }
  .contact li { display: flex; align-items: center; gap: 8px; height: 22px; }
  .contact .address { padding-left: 0; margin-bottom: 4px; }
  .contact svg { width: 13px; height: 13px; flex: none; fill: var(--icon); }
  .person {
    position: absolute; right: 78px; top: 198px; text-align: right;
  }
  .person-name { font-size: 19px; font-weight: 700; color: var(--brand-blue); }
  .person-role { font-size: 14px; color: var(--orange); margin-top: 2px; }

  /* Back */
  .card-back {
    left: 620px;
    background: linear-gradient(160deg, var(--sky-top), var(--sky-bottom));
    color: var(--white);
  }
  .back-title {
    position: absolute; left: 30px; top: 40px;
    font-size: 20px; font-weight: 700;
  }
  .services {
    position: absolute; left: 30px; top: 80px; list-style: none; font-size: 14px;
  }
  .services li { display: flex; align-items: center; gap: 10px; height: 28px; }
  .services svg { width: 16px; height: 16px; fill: var(--white); flex: none; }
  .insurance {
    position: absolute; left: 30px; top: 250px;
    font-size: 15px; font-weight: 700; letter-spacing: 0.3px;
  }
  .mascot {
    position: absolute; right: 24px; top: 10px; width: 170px; height: 200px;
    border-radius: 80px 80px 20px 20px;
    background: linear-gradient(180deg, var(--figure-a) 0%, var(--figure-a) 55%, var(--figure-b) 100%);
    opacity: 0.9;
  }
</style>
</head>
<body>

<section class="card card-front">
  <div class="brand">
    <span class="brand-dot"></span>
    <span class="brand-name">KTW Removals</span>
  </div>
  <div class="brand-sub">Pre Packing &amp; Storage</div>

  <ul class="contact">
    <li class="address">Burleigh Heads, QLD 4220</li>
    <li><svg viewBox="0 0 16 16"><path d="M3 1h3l1.5 4-2 1.3a9 9 0 0 0 4.2 4.2L11 8.5l4 1.5v3a2 2 0 0 1-2 2A12 12 0 0 1 1 3a2 2 0 0 1 2-2z"/></svg>07 5520 4316</li>
    <li><svg viewBox="0 0 16 16"><path d="M4 0h8a1 1 0 0 1 1 1v14a1 1 0 0 1-1 1H4a1 1 0 0 1-1-1V1a1 1 0 0 1 1-1zm1 2v10h6V2z"/></svg>0412 738 604</li>
    <li><svg viewBox="0 0 16 16"><rect x="1" y="1" width="14" height="14" rx="2"/></svg>/ktwremovals</li>
    <li><svg viewBox="0 0 16 16"><path d="M0 3h16v10H0zm1.5 1.2L8 9l6.5-4.8V4h-13z"/></svg>ktwremovals@mail.com</li>
    <li><svg viewBox="0 0 16 16"><circle cx="8" cy="8" r="7"/></svg>ktwremovals.com.au</li>
  </ul>

  <div class="person">
    <div class="person-name">Dane Whitlock</div>
    <div class="person-role">Owner Operator</div>
  </div>

  <div class="front-band"><span class="tagline">KTW Removals -The Gentle Movers.</span></div>
</section>

<section class="card card-back">
  <div class="mascot" role="img" aria-label="Cartoon removalist in cap and orange shirt giving a thumbs up beside a hand trolley"></div>
  <h2 class="back-title">KTW Removals Provides</h2>
  <ul class="services">
    <li><svg viewBox="0 0 16 16"><path d="M0 4h10v7H0zm10 2h3l3 3v2h-6z"/><circle cx="3" cy="12.5" r="1.5"/><circle cx="12" cy="12.5" r="1.5"/></svg>Local, Country &amp; Interstate Removals</li>
    <li><svg viewBox="0 0 16 16"><path d="M8 1l7 7h-2v7H9v-4H7v4H3V8H1z"/></svg>Home &amp; Hi rise removals</li>
    <li><svg viewBox="0 0 16 16"><path d="M2 15V3l6-2v14zm7 0V6l5 2v7z"/></svg>Office &amp; Factory Relocation's</li>
    <li><svg viewBox="0 0 16 16"><path d="M1 5l7-3 7 3v8l-7 3-7-3z"/></svg>Pre-packing &amp; Unpacking Services</li>
    <li><svg viewBox="0 0 16 16"><path d="M1 11h4l3 2h7v2H1zm4-9h7v7H5z"/></svg>Storage Solution</li>
  </ul>
  <div class="insurance">FREE TRANSIT INSURANCE</div>
</section>

</body>
</html>
```